New Web Design Project

Require a website for The Bramwell Harvest. All relevant information is in the uploaded files.

website to be responsive to work on mobile.

Required in html5, css

Coding

Coded - Design and coding required

Number of Pages Required

3 page

```html
<!DOCTYPE html>
<html lang="en">
<head>
<meta charset="utf-8">
<title>The Bramwell Harvest</title>
<link rel="stylesheet" href="https://fonts.googleapis.com/css2?family=Poppins:wght@300;400;500;600;700&display=swap">
<style>
:root{
  --green:#8cc63f;
  --orange:#f7941d;
  --ink:#333333;
  --ink-soft:#444444;
  --muted:#6a6a6a;
  --wash:#f7f8fc;
  --field:#ebebeb;
  --white:#ffffff;
}
*{box-sizing:border-box;margin:0;padding:0}
html,body{width:1200px;height:2933px;overflow:hidden;background:var(--white)}
body{font-family:'Poppins',sans-serif;color:var(--ink)}
a{text-decoration:none}
.page{position:relative;width:1200px;height:2933px;overflow:hidden}
.abs{position:absolute}

/* header */
.brand{position:absolute;display:flex;align-items:center;gap:10px}
.brand-dot{width:26px;height:26px;border-radius:50%;background:var(--orange);flex:none}
.brand-name{font-weight:700;font-size:22px;line-height:1;color:var(--ink-soft);white-space:nowrap}
.site-brand{left:89px;top:52px}
.main-nav{position:absolute;top:32px;right:88px;display:flex;gap:37px}
.main-nav a{font-weight:600;font-size:16px;color:var(--ink)}
.main-nav a.active{color:var(--orange)}

/* hero */
.hero-title{position:absolute;top:296px;left:0;width:1200px;text-align:center;font-weight:700;font-size:52px;line-height:51px;color:var(--ink-soft)}
.pill{position:absolute;display:flex;align-items:center;justify-content:center;border-radius:20px;color:var(--white);font-weight:600;font-size:14px;letter-spacing:.3px;text-transform:uppercase}
.hero-cta{left:526px;top:420px;width:148px;height:38px;background:var(--green)}
.produce{position:absolute;border-radius:50%}

/* about */
.wash{position:absolute;left:0;top:800px;width:1200px;height:677px;background:var(--wash)}
.about-mark{position:absolute;left:141px;top:880px;width:412px;height:490px;display:flex;flex-direction:column;align-items:center;justify-content:center;gap:34px}
.about-mark .big-dot{width:230px;height:230px;border-radius:50%;background:var(--orange)}
.about-mark .big-name{font-weight:700;font-size:36px;color:var(--green);text-align:center;line-height:1.15}
.about-copy{position:absolute;left:622px;top:940px;width:492px}
.section-title{font-weight:700;font-size:46px;color:var(--ink-soft);line-height:1.2}
.about-copy p{font-weight:300;font-size:15.6px;line-height:24px;color:var(--ink);margin-top:7px}
.about-copy .section-title{margin-bottom:4px}

/* team */
.team-title{position:absolute;top:1574px;left:0;width:1200px;text-align:center}
.member{position:absolute;top:1729px;width:300px;text-align:center}
.member-photo{width:258px;height:258px;border-radius:50%;margin:0 auto;padding:14px}
.member-photo .fill{width:100%;height:100%;border-radius:50%}
.member-name{margin-top:20px;font-weight:600;font-size:24px;color:var(--ink-soft)}
.member-role{font-weight:400;font-size:17px;color:var(--muted);line-height:1.3}

/* contact */
.contact-title{position:absolute;top:2144px;left:0;width:1200px;text-align:center}
.field{position:absolute;height:40px;border:none;border-radius:20px;background:var(--field);padding:0 22px;font-family:'Poppins',sans-serif;font-weight:500;font-size:14px;color:var(--muted)}
.field::placeholder{color:var(--muted)}
textarea.field{height:187px;padding:18px 22px;resize:none;border-radius:24px}
.submit{left:526px;top:2508px;width:148px;height:34px;background:var(--orange);border:none;font-family:'Poppins',sans-serif}

/* footer */
.to-top{position:absolute;left:580px;top:2678px;width:40px;height:40px;border-radius:50%;background:var(--orange);display:flex;align-items:center;justify-content:center}
.footer-brand{left:89px;top:2752px;flex-direction:column;align-items:flex-start;gap:12px}
.footer-brand .brand-dot{width:40px;height:40px;background:var(--white);margin-left:48px}
.footer-brand .brand-name{color:var(--white);font-size:22px}
.footer-nav{position:absolute;left:373px;top:2803px;display:flex;gap:36px}
.footer-nav a{font-weight:600;font-size:15.5px;color:var(--white)}
.copyright{position:absolute;left:370px;top:2829px;font-weight:600;font-size:15.5px;color:var(--white)}
.social{position:absolute;top:2814px;left:918px;display:flex;gap:8px}
.social span{width:42px;height:42px;border-radius:50%;background:rgba(0,0,0,.12)}
</style>
</head>
<body>
<div class="page">

  <!-- header -->
  <div class="brand site-brand"><span class="brand-dot"></span><span class="brand-name">The Bramwell Harvest</span></div>
  <nav class="main-nav">
    <a class="active" href="#">Home</a><a href="#">About</a><a href="#">Produce</a><a href="#">News</a><a href="#">Contact Us</a>
  </nav>

  <!-- hero produce -->
  <div class="produce" role="img" aria-label="Bunch of dark grapes with vine leaf" style="left:-20px;top:148px;width:134px;height:165px;background:radial-gradient(circle at 60% 30%,#7db03c 0 30%,#3a3550 55%,#2a2538 100%)"></div>
  <div class="produce" role="img" aria-label="Fresh strawberry" style="left:214px;top:262px;width:104px;height:118px;border-radius:48% 48% 50% 50%;background:radial-gradient(circle at 45% 45%,#e23a3a,#b3151d)"></div>
  <div class="produce" role="img" aria-label="Halved kiwi fruit" style="left:964px;top:144px;width:80px;height:78px;background:radial-gradient(circle,#e7efb8 0 18%,#a9c63a 40%,#6d8a2a 100%)"></div>
  <div class="produce" role="img" aria-label="Romaine lettuce leaves" style="left:1060px;top:108px;width:180px;height:234px;border-radius:50% 0 0 60%;background:linear-gradient(135deg,#b9dc6a,#4f8f2a)"></div>
  <div class="produce" role="img" aria-label="Green cabbage" style="left:-40px;top:421px;width:154px;height:154px;background:radial-gradient(circle at 40% 40%,#cfe8a4,#7cb24a)"></div>
  <div class="produce" role="img" aria-label="Red and green chilli peppers" style="left:190px;top:560px;width:345px;height:205px;border-radius:40%;background:linear-gradient(160deg,#6aa12e 0 35%,#d42a1f 45%,#b8d14a 70%,#8cba2e)"></div>
  <div class="produce" role="img" aria-label="Cloth bag filled with citrus, corn and vegetables" style="left:700px;top:478px;width:256px;height:296px;border-radius:45% 45% 50% 50%;background:radial-gradient(circle at 50% 45%,#f6b73c 0 30%,#a9c450 50%,#efe9dc 72%)"></div>
  <div class="produce" role="img" aria-label="Halved orange" style="left:1100px;top:507px;width:200px;height:284px;background:radial-gradient(circle at 40% 50%,#ffb43a,#f08a10)"></div>

  <h1 class="hero-title">The Best Produce<br>Delivered Daily</h1>
  <a class="pill hero-cta" href="#">Contact Us</a>

  <!-- about -->
  <svg class="abs" style="left:0;top:730px" width="1200" height="72" viewBox="0 0 1200 72" aria-hidden="true">
    <path d="M0 50 C 350 85, 800 82, 1200 8 L1200 72 L0 72 Z" fill="#f7f8fc"/>
  </svg>
  <section class="wash"></section>
  <div class="about-mark">
    <span class="big-dot"></span>
    <span class="big-name">The Bramwell Harvest</span>
  </div>
  <div class="about-copy">
    <h2 class="section-title">About Us</h2>
    <p>The Bramwell Harvest was incorporated with the objective of introducing new vendors to the Canadian market through a trusted and mutual business relation</p>
    <p>It was set up by Corin Halvey and Theo Marchetti who have a combined experience of over 45 years in the fresh produce business. With Corin's expertise in global sourcing and Theo's vast connection and know how of the Canadian market, we have helped our existing partners grow and expand their reach in the Canadian fresh produce market.</p>
    <p>Our expertise and supply chain knowledge allow us to develop programs and introduce new products to the Canadian consumer, via retail and wholesale channels across Canada.</p>
    <p>Get in touch to discuss how we can add value to your business</p>
  </div>

  <!-- team -->
  <h2 class="section-title team-title">Our Team</h2>
  <div class="member" style="left:244px">
    <div class="member-photo" style="background:linear-gradient(90deg,var(--green) 0 50%,transparent 50%)">
      <div class="fill" role="img" aria-label="Portrait of Corin Halvey" style="background:linear-gradient(180deg,#d9d9d9,#7a7a7a 60%,#2a2a2a)"></div>
    </div>
    <div class="member-name">Corin Halvey</div>
    <div class="member-role">Founder &amp; President</div>
  </div>
  <div class="member" style="left:624px">
    <div class="member-photo" style="background:linear-gradient(270deg,var(--orange) 0 50%,transparent 50%)">
      <div class="fill" role="img" aria-label="Portrait of Theo Marchetti" style="background:linear-gradient(180deg,#8a8580,#5c5854 55%,#1f2228)"></div>
    </div>
    <div class="member-name">Theo Marchetti</div>
    <div class="member-role">Founder</div>
  </div>

  <!-- contact -->
  <h2 class="section-title contact-title">Contact Us</h2>
  <form>
    <input class="field" style="left:355px;top:2212px;width:243px" placeholder="Name">
    <input class="field" style="left:603px;top:2212px;width:243px" placeholder="Email">
    <input class="field" style="left:355px;top:2260px;width:243px" placeholder="Phone number">
    <input class="field" style="left:603px;top:2260px;width:243px" placeholder="Service">
    <textarea class="field" style="left:356px;top:2309px;width:488px" placeholder="Message"></textarea>
    <button class="pill submit" type="submit">Submit</button>
  </form>

  <!-- footer -->
  <svg class="abs" style="left:0;top:2560px" width="1200" height="373" viewBox="0 0 1200 373" aria-hidden="true">
    <path d="M0 112 C 320 150, 620 175, 900 120 S 1140 60 1200 52 L1200 373 L0 373 Z" fill="#8cc63f"/>
    <path d="M0 48 C 300 25, 520 140, 800 118 C 980 104, 1100 70, 1200 52 L1200 64 C 1100 86, 960 132, 760 142 C 500 152, 300 76, 0 70 Z" fill="#f7941d"/>
  </svg>
  <div class="produce" role="img" aria-label="Pomegranates, one halved" style="left:-30px;top:2522px;width:200px;height:182px;background:radial-gradient(circle at 35% 55%,#e8526a 0 30%,#a31d2e 60%,#6b1420)"></div>
  <div class="produce" role="img" aria-label="Guava and ripe mango" style="left:1050px;top:2459px;width:180px;height:222px;border-radius:45%;background:linear-gradient(160deg,#f4b8c0 0 30%,#7aa63a 35%,#f5c22a 55%,#f0a10f)"></div>
  <a class="to-top" href="#" aria-label="Back to top">
    <svg width="12" height="8" viewBox="0 0 12 8"><path d="M1 7 L6 2 L11 7" fill="none" stroke="#fff" stroke-width="2"/></svg>
  </a>
  <div class="brand footer-brand"><span class="brand-dot"></span><span class="brand-name">The Bramwell Harvest</span></div>
  <nav class="footer-nav">
    <a href="#">Home</a><a href="#">About</a><a href="#">Produce</a><a href="#">News</a><a href="#">Contact Us</a>
  </nav>
  <div class="copyright">Copyright 2020 | All Rights Reserved</div>
  <div class="social">
    <span role="img" aria-label="Social profile link"></span>
    <span role="img" aria-label="Social profile link"></span>
    <span role="img" aria-label="Social profile link"></span>
    <span role="img" aria-label="Social profile link"></span>
  </div>
</div>
</body>
</html>
```